Business Card Design Project

Business card design with a funky, clean, modern design. Business is an immigration consultancy. Client base will be Canadian employers wanting to hire or retain foreign workers and foreign nationals wanting to immigrate to Canada.

Full color possible, but should incorporate red/white/black as per the logo to be provided. Double sided card design.

Target Market(s)

Canadian employers looking to hire/retain staff and also foreign nationals immigrating to Canada

Industry/Entity Type

Business

Requirements
Must have
• Logo (to be provided)
Name (Marla Quintero, Immigration Consultant)
Phone (604) 517-3362
E-mail: marla@lanternpathvisas.example
Web: www.lanternpathvisas.example

Nice to have
• Tag Line
Clean, modern style

```html
<!DOCTYPE html>
<html lang="en">
<head>
<meta charset="utf-8">
<title>Lantern Path Visas – Business Card</title>
<link rel="stylesheet" href="https://fonts.googleapis.com/css2?family=Open+Sans:wght@400;600;700&family=Questrial&family=Crimson+Text:ital@1&display=swap">
<style>
  :root {
    --canvas: #e9e7e4;
    --brand-red: #d6232f;
    --brand-red-dark: #a5121c;
    --ink: #1b1b1b;
    --ink-soft: #444;
    --band-text: #f3c9cc;
  }
  * { box-sizing: border-box; margin: 0; padding: 0; }
  html, body { width: 1200px; height: 646px; overflow: hidden; }
  body {
    background: var(--canvas);
    font-family: "Open Sans", Arial, sans-serif;
    color: var(--ink);
    position: relative;
  }
  .card {
    position: absolute;
    top: 169px;
    width: 540px;
    height: 308px;
    overflow: hidden;
    box-shadow: 0 6px 18px rgba(0,0,0,.18);
  }
  .card--front { left: 40px; }
  .card--back { left: 620px; }
  .card-art { position: absolute; inset: 0; width: 100%; height: 100%; }

  .brand-mark {
    position: absolute;
    display: flex;
    align-items: center;
    gap: 8px;
    font-weight: 600;
    text-transform: uppercase;
    letter-spacing: .08em;
    white-space: nowrap;
  }
  .brand-mark__dot { border-radius: 50%; background: currentColor; flex: none; }

  .brand-mark--hero { left: 0; right: 0; top: 118px; justify-content: center; color: var(--brand-red); font-size: 24px; }
  .brand-mark--hero .brand-mark__dot { width: 22px; height: 22px; }
  .brand-mark--band { color: var(--band-text); font-size: 10px; gap: 5px; }
  .brand-mark--band .brand-mark__dot { width: 10px; height: 10px; }
  .card--front .brand-mark--band { left: 22px; top: 22px; }
  .card--back .brand-mark--band { right: 22px; top: 18px; }

  .office-line {
    position: absolute; left: 0; right: 0; top: 160px;
    text-align: center; font-size: 10px; color: var(--ink-soft);
  }

  .holder-name {
    position: absolute; left: 26px; top: 176px;
    font-family: "Questrial", "Century Gothic", sans-serif;
    font-weight: 400;
    font-size: 34px; line-height: 1; letter-spacing: -.01em;
    white-space: nowrap;
  }
  .holder-name__first { color: var(--brand-red); }
  .holder-name__last { color: var(--ink); }
  .holder-title {
    position: absolute; left: 28px; top: 216px;
    font-weight: 700; font-size: 15px; color: var(--ink); letter-spacing: .02em;
  }

  .tagline {
    position: absolute; right: 30px; top: 80px;
    font-family: "Crimson Text", Georgia, serif; font-style: italic;
    font-size: 11.5px; line-height: 1.25; color: var(--ink-soft); text-align: left;
  }

  .contact-list {
    position: absolute; left: 318px; top: 138px;
    list-style: none; font-size: 12px; line-height: 1;
  }
  .contact-list li { display: flex; align-items: center; gap: 7px; margin-bottom: 6px; }
  .contact-list .contact-phone { font-weight: 700; font-size: 15px; }
  .contact-icon { width: 12px; height: 12px; flex: none; }
</style>
</head>
<body>

<section class="card card--front" aria-label="Card front">
  <svg class="card-art" viewBox="0 0 540 308" preserveAspectRatio="none" aria-hidden="true">
    <defs>
      <radialGradient id="frontSheen" cx="55%" cy="45%" r="75%">
        <stop offset="0" stop-color="#ffffff"/>
        <stop offset="1" stop-color="#d4d4d4"/>
      </radialGradient>
      <linearGradient id="frontRed" x1="0" y1="0" x2="1" y2="1">
        <stop offset="0" stop-color="#e23a44"/>
        <stop offset="1" stop-color="#a5121c"/>
      </linearGradient>
    </defs>
    <rect width="540" height="308" fill="url(#frontSheen)"/>
    <path d="M0,0 H540 V10 C420,30 230,70 0,112 Z" fill="url(#frontRed)"/>
    <path d="M0,112 C230,70 420,30 540,10" fill="none" stroke="#1b1b1b" stroke-width="3"/>
    <path d="M0,104 C230,62 420,22 540,2" fill="none" stroke="#ffffff" stroke-opacity=".25" stroke-width="2"/>
  </svg>
  <div class="brand-mark brand-mark--band"><span class="brand-mark__dot"></span>Lantern Path Visas</div>
  <div class="brand-mark brand-mark--hero"><span class="brand-mark__dot"></span>Lantern Path Visas</div>
  <p class="office-line">"Offices in Cedar Bluff, Harrow Point and Westhaven"</p>
</section>

<section class="card card--back" aria-label="Card back">
  <svg class="card-art" viewBox="0 0 540 308" preserveAspectRatio="none" aria-hidden="true">
    <defs>
      <radialGradient id="backSheen" cx="50%" cy="45%" r="75%">
        <stop offset="0" stop-color="#ffffff"/>
        <stop offset="1" stop-color="#d2d2d2"/>
      </radialGradient>
      <linearGradient id="backRed" x1="0" y1="0" x2="1" y2="1">
        <stop offset="0" stop-color="#c61a25"/>
        <stop offset="1" stop-color="#e53a44"/>
      </linearGradient>
      <linearGradient id="cornerRed" x1="0" y1="1" x2="1" y2="0">
        <stop offset="0" stop-color="#f2a0a5"/>
        <stop offset=".5" stop-color="#e03640"/>
        <stop offset="1" stop-color="#b3141e"/>
      </linearGradient>
    </defs>
    <rect width="540" height="308" fill="url(#backSheen)"/>
    <path d="M0,0 H540 V62 C380,66 180,52 0,32 Z" fill="url(#backRed)"/>
    <path d="M0,34 C180,54 380,68 540,64" fill="none" stroke="#1b1b1b" stroke-width="4"/>
    <path d="M230,308 C350,274 455,232 540,210 V308 Z" fill="url(#cornerRed)"/>
    <path d="M230,308 C350,274 455,232 540,210" fill="none" stroke="#1b1b1b" stroke-width="4"/>
  </svg>
  <div class="brand-mark brand-mark--band"><span class="brand-mark__dot"></span>Lantern Path Visas</div>

  <p class="tagline">"Clear guidance.<br>&nbsp;Open borders.<br>&nbsp;&nbsp;Lasting new beginnings"</p>

  <h1 class="holder-name"><span class="holder-name__first">Marla</span><span class="holder-name__last">Quintero</span></h1>
  <p class="holder-title">RCIC</p>

  <ul class="contact-list">
    <li class="contact-phone">
      <svg class="contact-icon" viewBox="0 0 12 12" aria-hidden="true"><rect x="3" y=".5" width="6" height="11" rx="1.2" fill="none" stroke="#1b1b1b"/><line x1="5" y1="9.5" x2="7" y2="9.5" stroke="#1b1b1b"/></svg>
      (604) 517-3362
    </li>
    <li>
      <svg class="contact-icon" viewBox="0 0 12 12" aria-hidden="true"><rect x=".5" y="2.5" width="11" height="7" fill="none" stroke="#1b1b1b"/><path d="M.5,2.5 L6,7 L11.5,2.5" fill="none" stroke="#1b1b1b"/></svg>
      marla@lanternpathvisas.example
    </li>
    <li>
      <svg class="contact-icon" viewBox="0 0 12 12" aria-hidden="true"><circle cx="6" cy="6" r="5.5" fill="#444"/><path d="M.5,6 H11.5 M6,.5 C3,3 3,9 6,11.5 M6,.5 C9,3 9,9 6,11.5" fill="none" stroke="#fff" stroke-width=".7"/></svg>
      www.lanternpathvisas.example
    </li>
  </ul>
</section>

</body>
</html>
```